Design mobile friendly review and ranking site

We're working on a corporate website for reviewing and ranking fellow employees. We need the website to look both fun and professional and it needs to be responsive - to it works on mobile and desktop.

Looking for css and HTML for 3 key pages as well as a header and footer for the site. Also would need any supporting graphics as part of the design.

Target Market(s)

Professionals in their 20s, 30s, and 40s.

Industry/Entity Type

Internet

Coding

Coded - Design and coding required

Number of Pages Required

3 page

Font styles to use
Sans Serif

Requirements
Must have
• 3 key pages we need (note included screenshots for each - these are just super rough cuts so you see examples of the content.)
• a) main-intro: A compelling into page with a login/registration form. Should be sleek/modern/enticing. Also we would show the ranking for the top 3 people to tease people re: content.
• b) main-page: Has two sections: One at the top where you would rate someone and one at the bottom where it shows a ranking of people.
• c) profile page: This is where you view a specific person. You see the person's picture, some info about the person, you see their overall rating, you can rate them, and you also see their historical ratings.
Nice to have
• Note we need css and HTML for this. It should feel as sleek and modern. Note also must be responsive design so it works well in mobile and desktop.

```html
<!DOCTYPE html>
<html lang="en">
<head>
<meta charset="utf-8">
<title>Peerly – Team Rankings</title>
<link rel="stylesheet" href="https://fonts.googleapis.com/css2?family=Raleway:wght@400;500;600&display=swap">
<style>
:root{
  --white:#ffffff;
  --ink:#222222;
  --page:#e3e7ea;
  --gold:#f1d95a;
  --brand-dot:#f0b400;
  --login:#35e03a;
  --sky:#12b8f2;
  --bar-top:#3af23f;
  --bar-bottom:#13b318;
  --bar-edge:#0c7f10;
  --name:#1d7a1d;
  --label-green:#2aa52a;
  --star:#f7a10c;
  --cta:#19d21d;
  --rule:#e2e2e2;
}
*{box-sizing:border-box;margin:0;padding:0}
html,body{width:902px;height:1200px;overflow:hidden}
body{font-family:"Raleway",sans-serif;font-variant-numeric:lining-nums;background:var(--page);color:var(--ink);position:relative}

.site-header{position:absolute;left:0;top:0;width:902px;height:78px;background:var(--white);border-bottom:1px solid #cfcfcf}
.brand{position:absolute;left:62px;top:24px;display:flex;align-items:center;gap:9px}
.brand-dot{width:14px;height:14px;border-radius:50%;background:var(--brand-dot)}
.brand-name{font-size:24px;font-weight:500;color:var(--ink)}
.header-link{position:absolute;right:60px;top:30px;font-size:13.5px;color:#333}

.hero{position:absolute;left:0;top:78px;width:902px;height:389px;
  background:linear-gradient(180deg,#2b2926 0%,#3a2a26 45%,#4b2a25 75%,#3d3a33 100%)}
.hero-shade{position:absolute;inset:0;background:radial-gradient(ellipse at 50% 40%,rgba(90,60,50,.35),rgba(0,0,0,.25))}
.hero-title{position:absolute;left:0;width:902px;text-align:center;font-weight:400}
.hero-title.line-one{top:74px;font-size:32.5px;color:var(--gold)}
.hero-title.line-two{top:118px;font-size:38px;color:var(--white)}
.hero-title .login{color:var(--login)}
.hero-title .register{color:var(--sky)}
.email-label{position:absolute;top:193px;left:0;width:902px;text-align:center;font-size:19px;color:var(--white)}
.email-input{position:absolute;left:253px;top:238px;width:217px;height:50px;background:var(--white);border:1px solid #ddd}
.register-button{position:absolute;left:493px;top:238px;width:157px;height:50px;background:var(--sky);color:var(--white);
  font-size:21px;display:flex;align-items:center;justify-content:center}

.filter-bar{position:absolute;left:60px;top:424px;width:782px;height:52px;
  background:linear-gradient(180deg,var(--bar-top),var(--bar-bottom))}
.bar-fold{position:absolute;top:468px}
.filter-select{position:absolute;left:291px;top:11px;width:145px;height:34px;background:var(--white);
  font-size:14px;color:var(--ink);padding-left:15px;display:flex;align-items:center}
.filter-select svg{position:absolute;right:12px;top:13px}
.filter-label{position:absolute;left:447px;top:20px;font-size:14px;color:var(--white)}

.ranking-card{position:absolute;left:60px;top:528px;width:782px;height:515px;background:var(--white)}
.rank-row{position:absolute;left:0;width:782px;height:161px}
.rank-row + .rank-row::before{content:"";position:absolute;left:7px;right:8px;top:0;border-top:1px solid var(--rule)}
.portrait-frame{position:absolute;left:27px;top:34px;width:112px;height:118px;border:1px solid #cfcfcf;padding:5px}
.portrait{width:100%;height:100%}
.rank-info{position:absolute;left:163px;top:50px;font-size:14px}
.rank-place{color:var(--ink)}
.rank-name{color:var(--name);font-weight:600;margin-top:2px;letter-spacing:.2px}
.rank-points{margin-top:20px}
.rank-points .value{color:var(--sky);font-weight:500}
.rank-reviews{margin-top:9px}
.rank-reviews .details{font-size:9.5px;color:#2e9f2e;margin-left:2px}
.rank-scores{position:absolute;right:20px;top:60px;display:grid;grid-template-columns:auto auto;column-gap:9px;row-gap:3px;align-items:center}
.score-label{text-align:right;font-size:14px}
.score-label.smarts{color:var(--sky)}
.score-label.easy{color:var(--ink)}
.score-label.hard{color:var(--label-green)}
.stars{color:var(--star);font-size:22px;letter-spacing:-0.5px;line-height:22px}

.teaser{position:absolute;left:200px;top:1070px;width:90px;height:90px;border-radius:50%;
  background:radial-gradient(circle at 40% 35%,#fff27a,#f6c518 60%,#e09a08)}
.teaser-cta{position:absolute;left:309px;top:1106px;width:391px;height:40px;background:var(--cta);color:#0b3a0b;
  font-size:14px;display:flex;align-items:center;justify-content:center;gap:8px}
</style>
</head>
<body>

<header class="site-header">
  <div class="brand"><span class="brand-dot"></span><span class="brand-name">Peerly</span></div>
  <div class="header-link">Log In Or Register Below</div>
</header>

<section class="hero">
  <div class="hero-shade" role="img" aria-label="Runners crouched at the starting line of a running track"></div>
  <h1 class="hero-title line-one">To See How People Are Ranked In Your Company</h1>
  <h2 class="hero-title line-two"><span class="login">Login</span> Or <span class="register">Register</span> Below:</h2>
  <div class="email-label">Your Work Email :</div>
  <div class="email-input"></div>
  <div class="register-button">Register</div>
</section>

<svg class="bar-fold" style="left:48px" width="12" height="12" viewBox="0 0 12 12"><polygon points="12,0 12,12 0,0" fill="var(--bar-edge)"/></svg>
<svg class="bar-fold" style="left:842px" width="12" height="12" viewBox="0 0 12 12"><polygon points="0,0 12,0 0,12" fill="var(--bar-edge)"/></svg>
<div class="filter-bar">
  <div class="filter-select">Best
    <svg width="10" height="9" viewBox="0 0 10 9"><polygon points="0,0 10,0 5,9" fill="#555"/></svg>
  </div>
  <div class="filter-label">People</div>
</div>

<main class="ranking-card">
  <article class="rank-row" style="top:0">
    <div class="portrait-frame"><div class="portrait" role="img" aria-label="Portrait photo of Mara Wendell" style="background:linear-gradient(160deg,#8a8f94,#b07a55 50%,#6d6a6a)"></div></div>
    <div class="rank-info">
      <div class="rank-place"># 1&nbsp; Best</div>
      <div class="rank-name">Mara Wendell</div>
      <div class="rank-points">Point: <span class="value">15</span></div>
      <div class="rank-reviews">Number Of Reviews: 1 <span class="details">View Details</span></div>
    </div>
    <div class="rank-scores">
      <span class="score-label smarts">Smarts</span><span class="stars">★★★★★</span>
      <span class="score-label easy">Easy To Work With</span><span class="stars">★★★★★</span>
      <span class="score-label hard">Hard Worker</span><span class="stars">★★★★★</span>
    </div>
  </article>

  <article class="rank-row" style="top:161px">
    <div class="portrait-frame"><div class="portrait" role="img" aria-label="Portrait photo of Jonah Pruett" style="background:linear-gradient(160deg,#9fd3ec,#d7b197 50%,#2e3a4c)"></div></div>
    <div class="rank-info">
      <div class="rank-place"># 1&nbsp; Best</div>
      <div class="rank-name">Jonah Pruett</div>
      <div class="rank-points">Point: <span class="value">15</span></div>
      <div class="rank-reviews">Number Of Reviews: 1 <span class="details">View Details</span></div>
    </div>
    <div class="rank-scores">
      <span class="score-label smarts">Smarts</span><span class="stars">★★★★★</span>
      <span class="score-label easy">Easy To Work With</span><span class="stars">★★★★★</span>
      <span class="score-label hard">Hard Worker</span><span class="stars">★★★★★</span>
    </div>
  </article>

  <article class="rank-row" style="top:322px">
    <div class="portrait-frame"><div class="portrait" role="img" aria-label="Portrait photo of Talia Corbin" style="background:linear-gradient(160deg,#d9d9d9,#a8765a 50%,#222)"></div></div>
    <div class="rank-info">
      <div class="rank-place"># 1&nbsp; Best</div>
      <div class="rank-name">Talia Corbin</div>
      <div class="rank-points">Point: <span class="value">15</span></div>
      <div class="rank-reviews">Number Of Reviews: 1 <span class="details">View Details</span></div>
    </div>
    <div class="rank-scores">
      <span class="score-label smarts">Smarts</span><span class="stars">★★★★★</span>
      <span class="score-label easy">Easy To Work With</span><span class="stars">★★★★★</span>
      <span class="score-label hard">Hard Worker</span><span class="stars">★★★★★</span>
    </div>
  </article>
</main>

<div class="teaser" role="img" aria-label="Smiling cartoon face giving a thumbs up"></div>
<div class="teaser-cta">Want To See More Rankings? Login Or Register Above
  <svg width="10" height="14" viewBox="0 0 10 14"><path d="M5 13V2M1 6l4-4 4 4" stroke="#0b3a0b" stroke-width="1.6" fill="none"/></svg>
</div>

</body>
</html>
```